Visitenkarten für den Verkauf mediterraner Pflanzen
Zielgruppe
Verkauf winterharter mediterraner Pflanzen
Aufgabenstellung
Die Farben von der Homepage und eventuell die Schriftarten sollten übernommen werden um ein einheitliches Erscheinungsbild zu erzeugen

```html
<!DOCTYPE html>
<html lang="de">
<head>
<meta charset="utf-8">
<title>Verdessa Südgarten – Visitenkarten</title>
<link rel="stylesheet" href="https://fonts.googleapis.com/css2?family=Open+Sans:wght@400;600;700&display=swap">
<style>
  :root {
    --stage: #eceeef;
    --card-light: #f1f2f3;
    --leaf-light: #d9dcdf;
    --ink-dark: #2a2e39;
    --ink-mid: #3a3f4b;
    --leaf-dark: #474c58;
    --accent-green: #4fae66;
    --text-light: #f4f5f6;
    --text-dark: #2e3340;
  }
  * { box-sizing: border-box; margin: 0; padding: 0; }
  html, body { width: 1200px; height: 720px; overflow: hidden; }
  body {
    background: var(--stage);
    font-family: "Open Sans", Arial, sans-serif;
    position: relative;
  }
  .card {
    position: absolute;
    width: 520px;
    height: 300px;
    overflow: hidden;
    box-shadow: 0 6px 18px rgba(0,0,0,0.12);
  }
  .card--front { left: 50px; top: 210px; background: var(--card-light); }
  .card--back  { left: 630px; top: 210px; background: var(--ink-dark); }

  .leaf-backdrop { position: absolute; inset: 0; }
  .card--front .leaf-backdrop {
    background: radial-gradient(ellipse at 65% 20%, #ffffff 0%, var(--leaf-light) 55%, var(--card-light) 100%);
  }
  .card--back .leaf-backdrop {
    background: radial-gradient(ellipse at 60% 40%, var(--leaf-dark) 0%, var(--ink-mid) 45%, var(--ink-dark) 100%);
  }

  .brand {
    position: absolute;
    display: flex;
    align-items: center;
    gap: 12px;
  }
  .brand__dot { border-radius: 50%; flex: none; }
  .brand__name {
    font-weight: 600;
    letter-spacing: 0.12em;
    text-transform: uppercase;
    line-height: 1.15;
  }
  .card--front .brand { left: 24px; top: 26px; }
  .card--front .brand__dot { width: 42px; height: 42px; background: var(--accent-green); }
  .card--front .brand__name { color: var(--text-dark); font-size: 17px; }

  .card--back .brand { left: 120px; top: 104px; }
  .card--back .brand__dot { width: 78px; height: 78px; background: var(--text-light); }
  .card--back .brand__name { color: var(--text-light); font-size: 22px; }

  .person {
    position: absolute;
    right: 34px;
    top: 112px;
    text-align: left;
  }
  .person__name {
    font-weight: 700;
    font-size: 22px;
    letter-spacing: 0.02em;
    color: var(--text-dark);
    padding-bottom: 5px;
    border-bottom: 1.5px solid var(--text-dark);
  }
  .person__role {
    margin-top: 4px;
    font-size: 14px;
    letter-spacing: 0.04em;
    color: var(--accent-green);
    text-align: center;
  }

  .contact-band {
    position: absolute;
    left: 0; right: 0; bottom: 0;
    height: 92px;
    background: var(--ink-dark);
    display: flex;
    align-items: center;
    justify-content: space-around;
    padding: 0 14px;
  }
  .contact-item {
    display: flex;
    align-items: center;
    gap: 8px;
    color: var(--text-light);
    font-size: 12px;
    line-height: 1.35;
  }
  .contact-item svg { width: 18px; height: 18px; flex: none; }

  .web-address {
    position: absolute;
    right: 26px;
    bottom: 20px;
    color: var(--text-light);
    font-size: 14px;
    letter-spacing: 0.02em;
  }
</style>
</head>
<body>

<section class="card card--front" aria-label="Visitenkarte Vorderseite">
  <div class="leaf-backdrop" role="img" aria-label="Helles Fächerpalmenblatt als Hintergrundfoto"></div>

  <div class="brand">
    <span class="brand__dot"></span>
    <span class="brand__name">Verdessa<br>Südgarten</span>
  </div>

  <div class="person">
    <p class="person__name">KONRAD WILBRANDT</p>
    <p class="person__role">DIRECTOR</p>
  </div>

  <div class="contact-band">
    <div class="contact-item contact-item--address">
      <svg viewBox="0 0 24 24" fill="none" stroke="currentColor" stroke-width="1.8"><path d="M12 22s7-7.2 7-12.5A7 7 0 0 0 5 9.5C5 14.8 12 22 12 22z"/><circle cx="12" cy="9.5" r="2.6"/></svg>
      <span>Lindenweg 12<br>A – 8010 Musterdorf</span>
    </div>
    <div class="contact-item contact-item--phone">
      <svg viewBox="0 0 24 24" fill="none" stroke="currentColor" stroke-width="1.8"><path d="M5 3h4l2 5-2.5 1.5a11 11 0 0 0 6 6L16 13l5 2v4a2 2 0 0 1-2 2A16 16 0 0 1 3 5a2 2 0 0 1 2-2z"/></svg>
      <span>+43 (0)699 20583147</span>
    </div>
    <div class="contact-item contact-item--email">
      <svg viewBox="0 0 24 24" fill="none" stroke="currentColor" stroke-width="1.8"><rect x="3" y="5" width="18" height="14" rx="1"/><path d="M3 6l9 7 9-7"/></svg>
      <span>office@verdessa.at</span>
    </div>
  </div>
</section>

<section class="card card--back" aria-label="Visitenkarte Rückseite">
  <div class="leaf-backdrop" role="img" aria-label="Dunkles Fächerpalmenblatt als Hintergrundfoto"></div>

  <div class="brand">
    <span class="brand__dot"></span>
    <span class="brand__name">Verdessa<br>Südgarten</span>
  </div>

  <p class="web-address">www.verdessa.at</p>
</section>

</body>
</html>
```